Financial Advisor needs waiting room sign

I am a financial advisor that works with a number of accountants to develop prospects. I am looking for a 18"x24" sign to hang in their office waiting rooms to help develop prospect interest in my services. My original idea was to list all of our services in a jumbled way on the sign and on the bottom have something like "Confused? We have the answers?" "Questions - We have answers" Our logo on the bottom. While I think this is still a good idea when I try to design it - it does not work. I am open to other ideas. Here is a list of our services (list in no particular order) and I will attach our logo. List: Plovance, Plovance Supplement, Plovance Advantage, Truvely, Part A, Part B, Part D, Social Security, Turning 65, Annuities, Fixed Index Annuities, Rollovers, 401k, 403b, Investments, Stock Market, Mutual Funds, Term Insurance, Life Insurance, Final Expense, Long Term Care, Mortgage Protection, 403B / 457 Not for Profit Set Up, 403B / TSA Plans, Annuities, Asset Protection, Charitable Giving, College Funding, Estate Planning, Fixed Indexed Annuities, Guaranteed Income, IRA & 401(K) Assets and Planning, IRA, 401(K), 403(B) Rollovers, Lifetime Income Planning, Retirement Income Planning, Safe Money Options, Social Security, Tactical Asset Allocation

```html
<!DOCTYPE html>
<html lang="en">
<head>
<meta charset="utf-8">
<title>Harwell Capital – Waiting Room Sign</title>
<link href="https://fonts.googleapis.com/css2?family=Figtree:wght@300;400;600;700;800;900&display=swap" rel="stylesheet">
<style>
  :root {
    --paper: #f7f7f7;
    --green-dark: #4b7a33;
    --green-light: #6eaa3f;
    --ink: #444444;
  }
  html, body { margin: 0; padding: 0; overflow: hidden; }
  .sign {
    position: relative;
    width: 1180px;
    height: 1200px;
    background: var(--paper);
    font-family: "Figtree", sans-serif;
    overflow: hidden;
  }
  .sign * { margin: 0; }
  .brand {
    position: absolute;
    left: 196px;
    top: 62px;
    display: flex;
    align-items: center;
    gap: 12px;
  }
  .brand-mark {
    width: 40px;
    height: 40px;
    border-radius: 50%;
    background: var(--green-light);
  }
  .brand-name {
    font-size: 17px;
    font-weight: 800;
    color: var(--green-dark);
    letter-spacing: 0.5px;
    line-height: 1;
  }
  .brand-tagline {
    font-size: 9px;
    font-weight: 700;
    color: var(--green-dark);
    letter-spacing: 1.6px;
    text-transform: uppercase;
    margin-top: 3px;
    line-height: 1;
  }
  .web-address {
    position: absolute;
    right: 201px;
    top: 64px;
    font-size: 17px;
    font-weight: 700;
    letter-spacing: 3.5px;
    color: var(--green-dark);
    line-height: 1;
  }
  .cloud .term {
    position: absolute;
    line-height: 1;
    white-space: nowrap;
  }
  .cloud .term span + span { margin-left: 14px; }
  .centered { transform: translateX(-50%); text-align: center; }
  .dark { color: var(--green-dark); }
  .light { color: var(--green-light); }
  .ink { color: var(--ink); }
  .w3 { font-weight: 300; }
  .w4 { font-weight: 400; }
  .w7 { font-weight: 700; }
  .w8 { font-weight: 800; }
  .tight { letter-spacing: -1px; }
  .headline {
    position: absolute;
    left: 602px;
    top: 990px;
    transform: translateX(-50%);
    font-size: 92px;
    font-weight: 900;
    color: var(--ink);
    letter-spacing: -1px;
    line-height: 1;
    white-space: nowrap;
  }
  .subline {
    position: absolute;
    left: 602px;
    top: 1086px;
    transform: translateX(-50%);
    font-size: 26px;
    font-weight: 400;
    color: var(--green-dark);
    line-height: 1;
    white-space: nowrap;
  }
</style>
</head>
<body>
<main class="sign">
  <header>
    <div class="brand">
      <span class="brand-mark"></span>
      <div>
        <p class="brand-name">HARWELL CAPITAL</p>
        <p class="brand-tagline">Insurance and Financial Services</p>
      </div>
    </div>
    <p class="web-address">WWW.WEBSITE.COM</p>
  </header>

  <section class="cloud" aria-label="Services arranged as a question mark">
    <!-- top arc -->
    <p class="term centered light w7" style="left:600px;top:186px;font-size:18px">Retirement Income Planning</p>
    <p class="term centered dark w8" style="left:600px;top:208px;font-size:44px">Life Insurance</p>
    <p class="term centered w4" style="left:600px;top:258px;font-size:17px"><span class="light">Guaranteed Income</span><span class="ink">Estate Planning</span></p>
    <p class="term centered" style="left:600px;top:280px;font-size:34px"><span class="light w8 tight">ANNUITIES</span><span class="dark w7" style="font-size:16px">Tactical Asset Allocation</span></p>

    <!-- left arm -->
    <p class="term light w7" style="left:366px;top:320px;font-size:17px">Charitable Giving</p>
    <p class="term dark w8 tight" style="left:350px;top:342px;font-size:62px">401(K)</p>
    <p class="term light w8" style="left:352px;top:410px;font-size:19px">TERM INSURANCE</p>
    <p class="term ink w4" style="left:352px;top:433px;font-size:20px">Final Expense</p>

    <!-- right arm -->
    <p class="term dark w8" style="left:660px;top:320px;font-size:17px">SAFE MONEY OPTIONS</p>
    <p class="term light w4" style="left:682px;top:342px;font-size:18px">Fixed Index Annuities</p>
    <p class="term dark w8 tight" style="left:690px;top:364px;font-size:70px">403b</p>
    <p class="term light w8" style="left:692px;top:436px;font-size:34px">Plovance</p>
    <p class="term ink w7" style="left:662px;top:474px;font-size:16px">Plovance Supplement</p>

    <!-- curve into stem -->
    <p class="term dark w8" style="left:612px;top:494px;font-size:34px">Stock Market</p>
    <p class="term light w7" style="left:586px;top:532px;font-size:15px">Truvely · Part A · Part B · Part D</p>
    <p class="term dark w8" style="left:556px;top:552px;font-size:30px">SOCIAL SECURITY</p>
    <p class="term ink w4" style="left:540px;top:586px;font-size:15px">IRA &amp; 401(K) Assets and Planning</p>
    <p class="term light w8" style="left:532px;top:606px;font-size:24px">Mutual Funds</p>
    <p class="term ink w4" style="left:528px;top:634px;font-size:19px">Mortgage Protection</p>
    <p class="term light w4" style="left:520px;top:658px;font-size:22px">Long Term Care</p>
    <p class="term dark w7" style="left:518px;top:686px;font-size:13px">403B / 457 Not for Profit Set Up</p>
    <p class="term dark w8 tight" style="left:512px;top:704px;font-size:96px;line-height:0.9">IRA</p>
    <p class="term light w8" style="left:516px;top:794px;font-size:22px">TURNING 65</p>

    <!-- dot -->
    <p class="term centered light w8" style="left:597px;top:842px;font-size:18px">403B / TSA Plans</p>
    <p class="term centered dark w8" style="left:597px;top:864px;font-size:42px">INVESTMENTS</p>
    <p class="term centered light w7" style="left:597px;top:910px;font-size:17px">Asset Protection</p>
    <p class="term centered dark w8" style="left:597px;top:931px;font-size:38px">ROLLOVERS</p>
  </section>

  <footer>
    <h1 class="headline">Confused?</h1>
    <p class="subline">We have the answers?</p>
  </footer>
</main>
</body>
</html>
```